Text only wordpress site to capture emails

Refer to inspiration upload for list of sites that will be useful for you.

We need a site that will be used to capture emails from clients that follow us on social media. The site will be all text, pretty simple. I have a couple of text sites that I like and we can use them for an example.

Menu section will have home, archive, about.
Footer will have © and Website Privacy Policy | Legal and Policies
There will be some text on the home page and an email capture.

This site will be all text no pictures.

I discuss office politics so the text portions will have some questions and answers on this and then prompt for the visitor to subscribe to my email list.

The only purpose of the site is to build an email list from existing social media followers so the site will be pretty simple in and of itself.

• Text only, similar Q&A to uploaded pics.

I will use a template from mail lantern dotcom for email capture.

I like the simple couriernew font family that is on both sites supplied in the uploads.
• If you use any color it needs to be very minimal.

```html
<!DOCTYPE html>
<html lang="en">
<head>
<meta charset="utf-8">
<title>Company Name</title>
<link href="https://fonts.googleapis.com/css2?family=Courier+Prime:wght@400;700&family=Roboto:wght@300;400;500;700&display=swap" rel="stylesheet">
<style>
:root{
  --slate:#525a65;
  --ink:#2f3640;
  --text:#3b4048;
  --muted:#8a8f96;
  --line:#d6d8db;
  --soft:#f9f9f9;
  --white:#ffffff;
  --chip:#e6e8eb;
  --arrow:#b9bdc3;
  --mono:"Courier Prime","Courier New",monospace;
  --sans:"Roboto",Arial,sans-serif;
}
*{box-sizing:border-box;margin:0;padding:0}
html,body{width:1200px;height:2713px;overflow:hidden;background:var(--white)}
body{position:relative;font-family:var(--mono);color:var(--text)}
.wrap{position:absolute;left:148px;width:902px}

/* header */
.site-header{position:absolute;top:0;left:0;width:1200px;height:77px;background:var(--white)}
.brand{position:absolute;left:148px;top:24px;font-family:var(--sans);font-size:21px;font-weight:500;color:#111;letter-spacing:.3px}
.main-nav{position:absolute;left:742px;top:19px;display:flex;font-family:var(--sans);font-size:16px;color:#222}
.main-nav a{display:block;height:37px;line-height:37px;text-decoration:none;color:inherit}
.main-nav .home{width:98px;text-align:center;background:var(--chip);border-radius:3px;box-shadow:0 3px 6px rgba(0,0,0,.08)}
.main-nav .archive{margin-left:52px}
.main-nav .about{margin-left:59px}

/* hero */
.hero{position:absolute;top:77px;left:0;width:1200px;height:582px;background:var(--slate);color:var(--white);text-align:center}
.hero h1{position:absolute;top:108px;left:0;width:1200px;font-family:var(--sans);font-weight:300;font-size:38px;line-height:51px}
.hero h1 b{font-weight:700}
.hero p{position:absolute;top:232px;left:280px;width:640px;font-size:16px;line-height:29px}
.signup{position:absolute;left:364px;width:472px;height:50px;background:var(--white);border-radius:2px;box-shadow:0 4px 10px rgba(0,0,0,.15)}
.hero .signup{top:344px}
.signup .field{position:absolute;left:23px;top:0;line-height:50px;font-size:15px;color:#555}
.signup .btn{position:absolute;right:5px;top:5px;width:125px;height:40px;line-height:40px;text-align:center;background:var(--slate);color:var(--white);font-weight:700;font-size:15px;border-radius:2px}

/* faq */
.faq-title{top:713px;font-family:var(--sans);font-weight:500;font-size:28px;color:var(--ink)}
.faq{position:absolute;left:152px;top:790px;width:898px;list-style:none}
.faq li{position:relative;border-bottom:1px solid var(--line);font-size:16px;color:var(--text)}
.faq .q{position:relative;height:57px;line-height:57px;padding-left:4px}
.faq .icon{position:absolute;right:22px;top:14px;width:29px;height:29px}
.faq li.open{border-bottom:1px solid var(--line)}
.faq li.open .q{font-weight:700;border-bottom:1px solid #777;height:58px;line-height:58px}
.faq .a{padding:24px 40px 36px 22px;font-size:14px;line-height:22.5px;color:#666}

/* blog */
.blog{position:absolute;top:1521px;left:0;width:1200px;height:942px;background:var(--soft)}
.blog-title{position:absolute;left:149px;top:60px;font-family:var(--sans);font-weight:300;font-size:32px;color:var(--ink)}
.blog-title b{font-weight:500}
.search{position:absolute;left:806px;top:60px;width:244px;height:35px;background:#eeeff1;border-radius:3px;font-family:var(--sans);font-size:13px;color:#444;line-height:35px;padding-left:18px}
.search svg{position:absolute;right:18px;top:13px}
.blog-rule{position:absolute;left:150px;top:122px;width:900px;border-top:1px solid var(--line)}
.cards{position:absolute;left:150px;top:194px;display:grid;grid-template-columns:repeat(3,282px);grid-auto-rows:280px;column-gap:27px;row-gap:26px}
.card{position:relative;background:var(--white);border:1px solid #e2e4e7;border-radius:3px;padding:0 29px}
.card.featured{box-shadow:0 6px 14px rgba(0,0,0,.12)}
.card .tag{margin-top:29px;font-size:11px;color:#999}
.card h3{margin-top:9px;font-family:var(--mono);font-weight:400;font-size:16px;line-height:23px;color:#222}
.card p{margin-top:11px;font-size:12px;line-height:21px;color:#777}
.card .go{position:absolute;right:-1px;bottom:-1px;width:37px;height:37px;background:var(--arrow);display:flex;align-items:center;justify-content:center}
.card.featured .go{background:var(--slate)}
.more{position:absolute;left:539px;top:829px;width:123px;height:39px;line-height:39px;text-align:center;background:var(--slate);color:var(--white);font-weight:700;font-size:15px;border-radius:2px}

/* footer */
.footer-band{position:absolute;top:2463px;left:0;width:1200px;height:90px;background:var(--slate)}
.footer-band .signup{top:21px;box-shadow:none}
.foot-nav{position:absolute;top:2578px;font-family:var(--sans);font-size:16px;color:#333}
.foot-nav span{position:absolute;white-space:nowrap;transform:translateX(-50%)}
.social{position:absolute;top:2579px;left:0}
.social i{position:absolute;width:14px;height:14px;border:1.6px solid #333;border-radius:50%;transform:translateX(-50%)}
.foot-rule{position:absolute;top:2628px;left:148px;width:902px;border-top:1px solid #eceded}
.copyright{position:absolute;top:2652px;left:148px;font-size:14px;color:#333}
.legal{position:absolute;top:2652px;left:745px;font-size:14px;color:#333}
.legal a{color:inherit;text-decoration:none;border-bottom:1px solid #333}
.legal .sep{margin:0 16px}
</style>
</head>
<body>

<header class="site-header">
  <div class="brand">COMPANY LOGO</div>
  <nav class="main-nav">
    <a class="home" href="#">Home</a>
    <a class="archive" href="#">Archive</a>
    <a class="about" href="#">About</a>
  </nav>
</header>

<section class="hero">
  <h1>Lorem Ipsum is <b>Simply Dummy</b><br><b>Text of the Printing</b></h1>
  <p>Lorem Ipsum is simply dummy text of the printing and typesetting industry. Lorem Ipsum has been the industry's.</p>
  <div class="signup"><span class="field">Your Email Address</span><span class="btn">Subscribe</span></div>
</section>

<h2 class="wrap faq-title">Frequently Asked Questions</h2>

<ul class="faq">
  <li><div class="q">Lorem Ipsum is simply dummy text ?<svg class="icon" viewBox="0 0 29 29"><circle cx="14.5" cy="14.5" r="13.5" fill="none" stroke="#aaa"/><path d="M14.5 8v13M8 14.5h13" stroke="#aaa"/></svg></div></li>
  <li class="open"><div class="q">Lorem Ipsum is simply dummy text of the printing ?<svg class="icon" viewBox="0 0 29 29"><circle cx="14.5" cy="14.5" r="13.5" fill="none" stroke="#333" stroke-width="1.4"/><path d="M8 14.5h13" stroke="#333" stroke-width="1.4"/></svg></div>
    <div class="a">Lorem Ipsum is simply dummy text of the printing and typesetting industry. Lorem Ipsum has been the industry's standard dummy text ever since the 1500s, when an unknown printer took a galley of type and scrambled it to make a type specimen book. It has survived not only five centuries, but also the leap into electronic typesetting, remaining essentially unchanged. It has survived not only five centuries, but</div></li>
  <li><div class="q">Lorem Ipsum is simply dummy text of the printing and typesetting ?<svg class="icon" viewBox="0 0 29 29"><circle cx="14.5" cy="14.5" r="13.5" fill="none" stroke="#aaa"/><path d="M14.5 8v13M8 14.5h13" stroke="#aaa"/></svg></div></li>
  <li><div class="q">Lorem Ipsum is simply dummy text of the printing?<svg class="icon" viewBox="0 0 29 29"><circle cx="14.5" cy="14.5" r="13.5" fill="none" stroke="#aaa"/><path d="M14.5 8v13M8 14.5h13" stroke="#aaa"/></svg></div></li>
  <li><div class="q">Lorem Ipsum is simply dummy text of the printing ?<svg class="icon" viewBox="0 0 29 29"><circle cx="14.5" cy="14.5" r="13.5" fill="none" stroke="#aaa"/><path d="M14.5 8v13M8 14.5h13" stroke="#aaa"/></svg></div></li>
  <li><div class="q">Lorem Ipsum is simply dummy text of the printing and typesetting ?<svg class="icon" viewBox="0 0 29 29"><circle cx="14.5" cy="14.5" r="13.5" fill="none" stroke="#aaa"/><path d="M14.5 8v13M8 14.5h13" stroke="#aaa"/></svg></div></li>
  <li><div class="q">Lorem Ipsum is simply dummy text of the ?<svg class="icon" viewBox="0 0 29 29"><circle cx="14.5" cy="14.5" r="13.5" fill="none" stroke="#aaa"/><path d="M14.5 8v13M8 14.5h13" stroke="#aaa"/></svg></div></li>
  <li><div class="q" style="height:67px;line-height:64px">Lorem Ipsum is simply dummy text of the printing and typesetting ?<svg class="icon" style="top:18px" viewBox="0 0 29 29"><circle cx="14.5" cy="14.5" r="13.5" fill="none" stroke="#aaa"/><path d="M14.5 8v13M8 14.5h13" stroke="#aaa"/></svg></div></li>
</ul>

<section class="blog">
  <h2 class="blog-title">Latest <b>Blog</b></h2>
  <div class="search">Search<svg width="10" height="7" viewBox="0 0 10 7"><path d="M1 1l4 4 4-4" fill="none" stroke="#555" stroke-width="1.3"/></svg></div>
  <div class="blog-rule"></div>
  <div class="cards">
    <article class="card"><div class="tag">BLOG</div><h3>Lorem Ipsum is simply dummy text of the</h3><p>Lorem Ipsum is simply dummy text of the printing and typesetting industry. Lorem Ipsum has been the industry's standard dummy text ever since the 1500s,</p><span class="go"><svg width="14" height="14" viewBox="0 0 14 14"><path d="M1 7h12M8 2l5 5-5 5" fill="none" stroke="#fff" stroke-width="1.5"/></svg></span></article>
    <article class="card featured"><div class="tag">BLOG</div><h3>Lorem Ipsum is simply dummy text of the</h3><p>Lorem Ipsum is simply dummy text of the printing and typesetting industry. Lorem Ipsum has been the industry's standard dummy text ever since the 1500s,</p><span class="go"><svg width="14" height="14" viewBox="0 0 14 14"><path d="M1 7h12M8 2l5 5-5 5" fill="none" stroke="#fff" stroke-width="1.5"/></svg></span></article>
    <article class="card"><div class="tag">BLOG</div><h3>Lorem Ipsum is simply dummy text of the</h3><p>Lorem Ipsum is simply dummy text of the printing and typesetting industry. Lorem Ipsum has been the industry's standard dummy text ever since the 1500s,</p><span class="go"><svg width="14" height="14" viewBox="0 0 14 14"><path d="M1 7h12M8 2l5 5-5 5" fill="none" stroke="#fff" stroke-width="1.5"/></svg></span></article>
    <article class="card"><div class="tag">BLOG</div><h3>Lorem Ipsum is simply dummy text of the</h3><p>Lorem Ipsum is simply dummy text of the printing and typesetting industry. Lorem Ipsum has been the industry's standard dummy text ever since the 1500s,</p><span class="go"><svg width="14" height="14" viewBox="0 0 14 14"><path d="M1 7h12M8 2l5 5-5 5" fill="none" stroke="#fff" stroke-width="1.5"/></svg></span></article>
    <article class="card"><div class="tag">BLOG</div><h3>Lorem Ipsum is simply dummy text of the</h3><p>Lorem Ipsum is simply dummy text of the printing and typesetting industry. Lorem Ipsum has been the industry's standard dummy text ever since the 1500s,</p><span class="go"><svg width="14" height="14" viewBox="0 0 14 14"><path d="M1 7h12M8 2l5 5-5 5" fill="none" stroke="#fff" stroke-width="1.5"/></svg></span></article>
    <article class="card"><div class="tag">BLOG</div><h3>Lorem Ipsum is simply dummy text of the</h3><p>Lorem Ipsum is simply dummy text of the printing and typesetting industry. Lorem Ipsum has been the industry's standard dummy text ever since the 1500s,</p><span class="go"><svg width="14" height="14" viewBox="0 0 14 14"><path d="M1 7h12M8 2l5 5-5 5" fill="none" stroke="#fff" stroke-width="1.5"/></svg></span></article>
  </div>
  <div class="more">More</div>
</section>

<footer>
  <div class="footer-band">
    <div class="signup"><span class="field">Your Email Address</span><span class="btn">Subscribe</span></div>
  </div>
  <nav class="foot-nav">
    <span style="left:423px">Home</span>
    <span style="left:512px">Archive</span>
    <span style="left:601px">About</span>
  </nav>
  <div class="social" aria-label="Social links">
    <i style="left:720px"></i><i style="left:752px"></i><i style="left:788px"></i>
  </div>
  <div class="foot-rule"></div>
  <div class="copyright">Copyright 2021 Company Name</div>
  <div class="legal"><a href="#">Privacy Policy</a><span class="sep">|</span><a href="#">Legal and Policies</a></div>
</footer>

</body>
</html>
```